Sunbird Therapy Services needs upgraded website

Upgrade current website www.sunbirdtherapy.com.au. Need to incorporate new logo (attached). Family friendly and professional feel. Use of colour green. We are based in Melbourne, Australia and work with children aged 0-16 who have additional needs requiring therapy.

Target Market(s)

Parents of children with special needs.

Colors
000000

Requirements
Must have
• The current content/ pictures are already on the website and can be replicated, just with a fresh look. Additionally need an FAQ section. Must incorporate logo and have consistency on each page. Needs to be accessible on tablets/devices (current website only shows home page on devices, however actual sites has many sub pages (approx. 7). I will need to be able to easily edit the content down the track and potentially add pages.

```html
<!DOCTYPE html>
<html lang="en">
<head>
<meta charset="utf-8">
<title>Sunbird Therapy Services</title>
<link href="https://fonts.googleapis.com/css2?family=Oswald:wght@300;400&family=Raleway:wght@600;700&family=Roboto:wght@400;500&display=swap" rel="stylesheet">
<style>
:root{
  --green:#3aa83a;
  --green-deep:#1d5a23;
  --green-text:#2e8b2e;
  --dark:#113315;
  --orange:#f39a1a;
  --nav:#173a1b;
  --footer:#1b4a1f;
  --black:#111;
  --ink:#333;
  --white:#fff;
}
*{margin:0;padding:0;box-sizing:border-box}
html,body{width:730px;height:1200px;overflow:hidden;background:var(--white)}
body{position:relative;font-family:"Roboto",sans-serif;color:var(--ink)}
.abs{position:absolute}
.header{left:0;top:0;width:730px;height:105px;background:var(--green)}
.brand{left:58px;top:30px;display:flex;align-items:center;gap:8px}
.brand-mark{width:18px;height:18px;background:var(--dark)}
.brand-name{font-family:"Raleway",sans-serif;font-weight:700;font-size:22px;color:var(--dark);line-height:1}
.phone{right:56px;top:29px;display:flex;align-items:center;gap:8px;color:var(--white);font-size:15px}
.nav{left:53px;top:78px;width:624px;height:37px;background:linear-gradient(#234d27,var(--nav));display:flex;justify-content:space-between;padding-right:10px;box-shadow:0 2px 4px rgba(0,0,0,.3);overflow:hidden}
.nav a{font-family:"Oswald",sans-serif;font-weight:300;font-size:9.5px;color:var(--white);text-decoration:none;display:flex;align-items:center;white-space:nowrap}
.nav a.active{background:var(--orange);width:45px;justify-content:center}
.hero{left:0;top:104px;width:730px;height:318px;background:linear-gradient(180deg,#b9cde0 0%,#8c9aa6 25%,#6d6a66 55%,#4f4c48 100%)}
.hero-title{right:68px;top:140px;text-align:right;color:var(--white);font-family:"Oswald",sans-serif;text-shadow:0 1px 3px rgba(0,0,0,.5)}
.hero-title h1{font-weight:400;font-size:28px;line-height:1.1}
.hero-title p{font-weight:300;font-size:19px;margin-top:2px}
.arrow{width:14px;height:40px}
.welcome{left:0;top:422px;width:730px;height:170px;text-align:center}
.section-title{font-family:"Raleway",sans-serif;font-weight:700;font-size:15px;color:var(--dark)}
.section-title span{color:var(--green-text)}
.welcome h2{margin-top:37px}
.welcome p{width:590px;margin:10px auto 0;font-size:8px;line-height:16px;color:#222}
.btn{display:inline-block;margin-top:12px;width:72px;height:24px;line-height:22px;background:#4a9c4a;border:1px solid #2f7d2f;border-radius:2px;color:var(--white);font-size:8px;font-weight:500}
.services{left:0;top:592px;width:730px;height:234px;background:linear-gradient(#e9e9e9,#fafafa 40%,#f3f3f3);border-top:1px solid #ddd;border-bottom:1px solid #ddd}
.services h2{position:absolute;top:24px;width:100%;text-align:center}
.card{top:54px;width:150px}
.photo{border:3px solid var(--white);box-shadow:0 0 3px rgba(0,0,0,.35);height:92px}
.card h3{font-family:"Raleway",sans-serif;font-weight:600;font-size:9.5px;color:var(--green-deep);margin-top:13px}
.card p{width:132px;font-size:6.5px;line-height:11px;margin-top:3px;color:#444}
.card .more{font-size:7px;color:var(--green-text);margin-top:6px;display:block}
.group-photo{left:55px;top:864px;width:168px;height:116px;border:3px solid var(--white);box-shadow:0 0 3px rgba(0,0,0,.35)}
.group{left:237px;top:866px;width:254px}
.group p{font-size:7.2px;line-height:14px;margin-top:9px;color:#555}
.group .more{font-size:9px;color:var(--green-deep);display:block;margin-top:7px}
.news{left:516px;top:862px;width:161px}
.news h2{font-size:11px;padding-bottom:8px;border-bottom:1px solid #bbb}
.news-item{display:flex;gap:6px;margin-top:10px}
.date{width:28px;height:30px;border:1px solid #ddd;text-align:center;background:#fff;flex:none}
.date b{display:block;font-size:9px;line-height:19px;border-bottom:1px solid #ddd}
.date i{font-style:normal;font-size:5px;color:#888;background:#eee;display:block;line-height:10px}
.news-item h4{font-family:"Raleway",sans-serif;font-size:7px;color:var(--green-deep);font-weight:600}
.news-item p{font-size:6px;color:#666;margin-top:4px}
.dots{border-top:1px dotted #999;margin-top:8px;width:130px}
.footer{left:0;top:1013px;width:730px;height:145px;background:var(--footer);color:var(--white)}
.fcol{top:26px}
.fcol h3{font-family:"Oswald",sans-serif;font-weight:400;font-size:11px;margin-bottom:12px}
.fcol p{font-size:7px;line-height:11px}
.field{width:131px;height:19px;background:#eee;color:#666;font-size:6px;padding:6px;margin-top:6px}
.subscribe{display:inline-block;margin-top:7px;background:var(--black);color:var(--white);font-size:6.5px;font-weight:500;padding:5px 8px;border-radius:2px}
.social{display:flex;align-items:center;gap:12px;font-size:7px;margin-bottom:6px}
.circle{width:20px;height:20px;border-radius:50%;border:1px solid rgba(255,255,255,.35)}
.copy{left:0;top:1158px;width:730px;height:42px;background:var(--black);color:var(--white);font-size:7px;text-align:center;line-height:34px}
</style>
</head>
<body>
<header class="abs header">
  <div class="abs brand"><span class="brand-mark"></span><span class="brand-name">Sunbird Therapy Services</span></div>
  <div class="abs phone">
    <svg width="18" height="18" viewBox="0 0 18 18"><circle cx="9" cy="9" r="8" fill="none" stroke="#f6a623" stroke-width="1.5"/><path d="M6 5l2 2-1 1.3c.6 1.2 1.5 2.1 2.7 2.7L11 10l2 2-1.3 1.3C8.6 13 5 9.4 4.7 6.3z" fill="#f6a623"/></svg>
    (03) 9555 0182
  </div>
</header>
<nav class="abs nav">
  <a class="active" href="#">HOME</a><a href="#">OCCUPATIONAL THERAPY</a><a href="#">THERAPY SERVICES</a><a href="#">GROUP SESSIONS</a><a href="#">TRAINING PACKAGES</a><a href="#">MEET THE STAFF</a><a href="#">PARENT RESOURCES</a><a href="#">CONTACT US</a>
</nav>
<section class="abs hero" role="img" aria-label="Aerial photograph of the Melbourne city skyline and river">
  <svg class="abs arrow" style="left:34px;top:150px" viewBox="0 0 14 40"><path d="M13 1L1 20l12 19" fill="none" stroke="#fff" stroke-width="1.3"/></svg>
  <svg class="abs arrow" style="right:34px;top:150px" viewBox="0 0 14 40"><path d="M1 1l12 19L1 39" fill="none" stroke="#fff" stroke-width="1.3"/></svg>
  <div class="abs hero-title"><h1>SUNBIRD THERAPY SERVICES</h1><p>Ipsum is simply dummy text of the printing</p></div>
</section>
<section class="abs welcome">
  <h2 class="section-title">WELCOME TO <span>SUNBIRD THERAPY</span></h2>
  <p>Lorem Ipsum has been the industry's standard dummy text ever since the 1500s, when an unknown printer took a galley of type and scrambled it to make a type specimen book. It has survived not only five centuries, but also the leap into electronic typesetting, remaining essentially unchanged. It was popularised in the 1960s with the release of Letraset sheets containing Lorem Ipsum passages, and more recently with desktop publishing software</p>
  <span class="btn">READ MORE</span>
</section>
<section class="abs services">
  <h2 class="section-title">THERAPY <span>SERVICES</span></h2>
  <svg class="abs arrow" style="left:24px;top:80px" viewBox="0 0 14 40"><path d="M13 1L1 20l12 19" fill="none" stroke="#333" stroke-width="1"/></svg>
  <svg class="abs arrow" style="right:24px;top:80px" viewBox="0 0 14 40"><path d="M1 1l12 19L1 39" fill="none" stroke="#333" stroke-width="1"/></svg>
  <div class="abs card" style="left:56px"><div class="photo" role="img" aria-label="Therapist working with a young girl" style="background:linear-gradient(135deg,#2f5a3a,#3a5fb8 60%,#2a3f2e)"></div><h3>PERCEPTUAL SKILLS</h3><p>Lorem Ipsum is simply dummy text of the printing and typesetting industry</p><span class="more">Read More &gt;&gt;</span></div>
  <div class="abs card" style="left:213px"><div class="photo" role="img" aria-label="Toddler playing with a shape sorter" style="background:linear-gradient(135deg,#8a3a6a,#e43a8c 55%,#c6407f)"></div><h3>SOCIAL SKILLS</h3><p>Lorem Ipsum is simply dummy text of the printing and typesetting industry</p><span class="more">Read More &gt;&gt;</span></div>
  <div class="abs card" style="left:368px"><div class="photo" role="img" aria-label="Girl playing a connect-four game" style="background:linear-gradient(135deg,#5a4a3a,#c9b8a8 45%,#2b4fb5 75%)"></div><h3>COGNITIVE SKILLS</h3><p>Lorem Ipsum is simply dummy text of the printing and typesetting industry</p><span class="more">Read More &gt;&gt;</span></div>
  <div class="abs card" style="left:525px"><div class="photo" role="img" aria-label="Child drawing at a table" style="background:linear-gradient(135deg,#4a4a4a,#8a7a6a 55%,#6a5040)"></div><h3>SENSORY PROCESSING</h3><p>Lorem Ipsum is simply dummy text of the printing and typesetting industry</p><span class="more">Read More &gt;&gt;</span></div>
</section>
<div class="abs group-photo" role="img" aria-label="Young girl blowing bubbles outdoors" style="background:linear-gradient(120deg,#6a8a3a,#b8c86a 45%,#e8d8b8 70%,#7a9a4a)"></div>
<section class="abs group">
  <h2 class="section-title">GROUP SESSIONS</h2>
  <p>Lorem Ipsum has been the industry's standard dummy text ever since the 1500s, when an unknown printer took a galley of type and scrambled it to make a type specimen book. It has survived not only five centuries, but also the leap into electronic typesetting, remaining essentially unchanged. It was popularised in the 1960s with the release of Letraset sheets</p>
  <span class="more">Read More &gt;&gt;</span>
</section>
<aside class="abs news">
  <h2 class="section-title">LATEST NEWS</h2>
  <div class="news-item"><div class="date"><b>20</b><i>mar</i></div><div><h4>NEWS HEADLINE HERE</h4><p>Lorem ipsum dolor sit amet, consec-</p></div></div>
  <div class="dots"></div>
  <div class="news-item" style="margin-top:14px"><div class="date"><b>20</b><i>mar</i></div><div><h4>NEWS HEADLINE HERE</h4><p>Lorem ipsum dolor sit amet, consec-</p></div></div>
</aside>
<footer class="abs footer">
  <div class="abs fcol" style="left:55px"><h3>NEWSLETTERS SIGN UP</h3><p>Sign up for our daily email by entering<br>your information below</p><div class="field">Email address</div><span class="subscribe">SUBSCRIBE</span></div>
  <div class="abs fcol" style="left:236px"><h3>LATEST TWEET</h3><p style="display:flex;gap:5px;align-items:center"><span class="circle" style="width:10px;height:10px;background:#fff;border:0"></span>Featured Workspace : Bluebench</p><p style="margin:5px 0 0 17px"><i>snbd.io/7KpWz2"</i></p><p style="margin:5px 0 0 17px">10 hours ago</p></div>
  <div class="abs fcol" style="left:417px"><h3>GET IN TOUCH</h3><p>Address : 42 Wattle Grove Rd,<br>Kew, VIC</p><p style="margin-top:10px">Phone : 03 9555 0183</p><p style="margin-top:10px">Email : hello@sunbirdmail.com</p></div>
  <div class="abs fcol" style="left:587px"><h3>FOLLOW US ON</h3><div class="social"><span class="circle"></span>Friendpage</div><div class="social"><span class="circle"></span>Chirpline</div><div class="social"><span class="circle"></span>Snapframe</div></div>
</footer>
<div class="abs copy">Copyright © 2015. All Rights Reserved</div>
</body>
</html>
```